Dawson's Lawn Service needs a postcard design

I need a design to attract lawn cutting customers. I am a high school junior, focusing on my city and the neighboring city. I think it would be advantageous to let my potential clients know I am earning money for my college education. They should also know, I will be working side by side with my father, who operated his own lawn service for 20 years, so they can be assured of a quality result for their lawn. I will be using state of the art, commercial equipment.

A few things that are unique to my service are; my mower weighs half of what other commercial mowers do (a softer footprint), my mower does NOT throw clippings into mulch or flower beds, at an additional charge I offer bagging of the clippings and/or dog waste clean-up. I am thinking about a two-sided design. I would also like a cartoon style picture of myself riding my mower. If this is something you can create, I can send you a photo of myself and a photo of my mower. If not, I can get this drawing done separately, then send it to you, I would just need to know what kind of file you would need it in. I am not going to have a business name, I want to introduce myself as Dawson to keep it simple and personal. We can add a coupon to the postcard, offering one free cut with commitment to a full 26 week season. The name of my high school is Marwick High.

The cartoon picture attached is our logo.

Target Market(s)

Homeowners that use a commercial lawn cutting service, homeowners that need a temporary service while they are on vacation

Industry/Entity Type

School

Colors
3176b5
9bcb3c

Requirements
Must have
• An appeal for people to want to help me earn money for my college education. A clear idea they will be getting top notch service. I definitely want a drawing of myself on my mower. Phone # 555-271-0936
• design must work with parcelrelay.com/routeblanketmail guidelines

```html
<!DOCTYPE html>
<html lang="en">
<head>
<meta charset="utf-8">
<title>Dawson's Lawn Service Postcard</title>
<link rel="stylesheet" href="https://fonts.googleapis.com/css2?family=Roboto:wght@300;400;700;900&display=swap">
<style>
  :root {
    --page: #e9ebee;
    --card-blue: #2d6faf;
    --card-blue-deep: #245d96;
    --ink-navy: #173a60;
    --ink-light: #dce8f5;
    --paper: #ffffff;
    --line-grey: #c9ced4;
    --art-red: #d9465a;
    --art-grey: #9aa3ad;
  }
  * { box-sizing: border-box; margin: 0; padding: 0; }
  html, body { width: 1200px; height: 800px; overflow: hidden; }
  body {
    background: var(--page);
    font-family: "Roboto", Arial, sans-serif;
    position: relative;
  }

  /* ---------- Front side ---------- */
  .postcard-front {
    position: absolute;
    left: 30px; top: 170px;
    width: 590px; height: 460px;
    background: var(--card-blue);
    box-shadow: 0 6px 18px rgba(0,0,0,.18);
    overflow: hidden;
  }
  .offer-band {
    position: absolute;
    left: 0; top: 0;
    width: 96px; height: 100%;
    background: var(--card-blue-deep);
  }
  .offer-text {
    position: absolute;
    left: 48px; top: 230px;
    width: 440px;
    transform: translate(-50%, -50%) rotate(-90deg);
    text-align: center;
    color: var(--ink-navy);
  }
  .offer-title {
    font-size: 50px; font-weight: 900; line-height: 1;
    letter-spacing: .5px;
  }
  .offer-terms {
    font-size: 15px; font-weight: 700; margin-top: 4px;
  }
  .mower-portrait {
    position: absolute;
    left: 118px; top: 84px;
    width: 220px; height: 270px;
    border-radius: 10px;
    background: linear-gradient(160deg, var(--art-grey) 0%, #5c7e63 45%, var(--art-red) 100%);
    opacity: .9;
  }
  .brand-name {
    position: absolute;
    left: 250px; top: 26px;
    white-space: nowrap;
    color: var(--ink-navy);
    font-size: 44px; font-weight: 900; line-height: 1;
  }
  .brand-name span {
    font-size: 20px; font-weight: 400; margin-left: 6px;
  }
  .pitch {
    position: absolute;
    left: 356px; top: 92px;
    width: 210px;
    color: var(--ink-light);
    font-size: 12.5px; font-weight: 300; line-height: 1.3;
  }
  .pitch p + p { margin-top: 12px; }
  .school-name {
    position: absolute;
    left: 370px; top: 330px;
    color: var(--ink-navy);
    font-size: 26px; font-weight: 700;
    white-space: nowrap;
  }
  .front-phone {
    position: absolute;
    left: 118px; top: 388px;
    display: flex; align-items: center; gap: 12px;
    color: var(--ink-navy);
    font-size: 38px; font-weight: 700;
    white-space: nowrap;
  }

  /* ---------- Back side ---------- */
  .postcard-back {
    position: absolute;
    left: 650px; top: 220px;
    width: 520px; height: 340px;
    display: flex;
    box-shadow: 0 6px 18px rgba(0,0,0,.18);
  }
  .back-info {
    width: 46%;
    background: var(--card-blue);
    padding: 22px 20px;
    color: var(--ink-navy);
  }
  .back-brand {
    display: flex; align-items: center; gap: 10px;
  }
  .brand-dot {
    width: 34px; height: 34px; border-radius: 50%;
    background: var(--card-blue-deep);
    border: 2px solid var(--ink-navy);
    flex: none;
  }
  .back-brand-name {
    font-size: 24px; font-weight: 700; line-height: 1;
    white-space: nowrap;
  }
  .back-brand-name small {
    display: block; font-size: 11px; font-weight: 700; margin-top: 2px;
  }
  .contact-label {
    margin-top: 22px;
    font-size: 15px; font-weight: 700;
  }
  .back-phone {
    display: flex; align-items: center; gap: 8px;
    font-size: 19px; font-weight: 700; margin-top: 4px;
    white-space: nowrap;
  }
  .mailing-side {
    flex: 1;
    background: var(--paper);
    position: relative;
  }
  .stamp-box {
    position: absolute;
    right: 22px; top: 22px;
    width: 74px; height: 84px;
    border: 2px solid var(--line-grey);
  }
  .address-line {
    position: absolute;
    left: 22px; right: 22px;
    border-top: 1px solid var(--line-grey);
  }
  .address-line.first { top: 150px; }
  .address-line.second { top: 195px; }
  .address-line.third { top: 240px; }
</style>
</head>
<body>

  <section class="postcard-front">
    <div class="offer-band"></div>
    <div class="offer-text">
      <div class="offer-title">One Free Cut</div>
      <div class="offer-terms">with commitment to a full 26 week season</div>
    </div>

    <div class="mower-portrait" role="img" aria-label="Cartoon illustration of Dawson riding his red commercial mower"></div>

    <h1 class="brand-name">Dawson's<span>Lawn Service</span></h1>

    <div class="pitch">
      <p>My mower weighs half of what other commercial mowers do (a softer footprint), my mower does NOT throw clippings into mulch or flower beds, at an additional charge I offer bagging of the clippings and/or dog waste clean-up.</p>
      <p>I am a high school junior, focusing on my city and the neighboring city.</p>
      <p>I am earning money for my college education.</p>
    </div>

    <div class="school-name">Marwick High</div>

    <div class="front-phone">
      <svg width="32" height="32" viewBox="0 0 32 32" aria-hidden="true">
        <circle cx="16" cy="16" r="14" fill="none" stroke="currentColor" stroke-width="2.5"/>
        <path d="M11 9c1-1 2 0 3 2s0 2-1 3c1 2 3 4 5 5 1-1 1-2 3-1s3 2 2 3c-1 2-3 2-5 1-4-2-7-5-8-9 0-2 0-3 1-4z" fill="currentColor"/>
      </svg>
      <span>555-271-0936</span>
    </div>
  </section>

  <section class="postcard-back">
    <div class="back-info">
      <div class="back-brand">
        <div class="brand-dot"></div>
        <div class="back-brand-name">Dawson's<small>Lawn Service</small></div>
      </div>
      <div class="contact-label">Contact:</div>
      <div class="back-phone">
        <svg width="18" height="18" viewBox="0 0 32 32" aria-hidden="true">
          <circle cx="16" cy="16" r="14" fill="none" stroke="currentColor" stroke-width="2.5"/>
          <path d="M11 9c1-1 2 0 3 2s0 2-1 3c1 2 3 4 5 5 1-1 1-2 3-1s3 2 2 3c-1 2-3 2-5 1-4-2-7-5-8-9 0-2 0-3 1-4z" fill="currentColor"/>
        </svg>
        <span>555-271-0936</span>
      </div>
    </div>
    <div class="mailing-side">
      <div class="stamp-box"></div>
      <div class="address-line first"></div>
      <div class="address-line second"></div>
      <div class="address-line third"></div>
    </div>
  </section>

</body>
</html>
```